The title of the book is Beyond the Tidewater and the subtitle of the book is Walking Faith Through Rivers

I need a book cover that has a picture of a valley that is between two mountains. The picture needs to show mountains and a valley, not canyons and a valley. The focus should be on the valley. The attached covers are covers that I like with similar book titles. I would like for my name to be in all caps...DR. MARCUS J. HOLLOWAY

Target Market(s)

Religious: Christian: Spiritual: Ages 21 and up

Industry/Entity Type

Religious

Requirements
Must have
• I need to see mountains and a valley, not canyons and valleys. The designer must know the difference between a canyon and a mountain. Looking for a contemporary design.

```html
<!DOCTYPE html>
<html lang="en">
<head>
<meta charset="utf-8">
<title>Beyond the Tidewater — Book Cover</title>
<link rel="stylesheet" href="https://fonts.googleapis.com/css2?family=Cinzel:wght@500;600;700&family=Oswald:wght@500;600&display=swap">
<style>
  :root {
    --page-bg: #d7d7d5;
    --navy: #0f2a47;
    --navy-deep: #0b2340;
    --sky-top: #1f4f8c;
    --sky-mid: #1577b8;
    --sky-low: #7fb4dc;
    --rock-red: #8b4a2e;
    --rock-dark: #5e3020;
    --valley-green: #7f8d3c;
    --white: #ffffff;
    --rule: rgba(255,255,255,0.75);
  }
  * { margin: 0; padding: 0; box-sizing: border-box; }
  html, body { width: 800px; height: 1200px; overflow: hidden; }
  body {
    background: var(--page-bg);
    position: relative;
    font-family: "Cinzel", serif;
  }
  .book-spread {
    position: absolute;
    left: 39px;
    top: 191px;
    width: 722px;
    height: 818px;
    display: flex;
    gap: 41px;
  }
  .spine {
    width: 136px;
    height: 100%;
    background: var(--navy);
    box-shadow: 3px 4px 8px rgba(0,0,0,0.25);
    display: flex;
    align-items: center;
    justify-content: center;
  }
  .spine-text {
    writing-mode: vertical-rl;
    color: var(--white);
    font-family: "Cinzel", serif;
    font-weight: 600;
    font-size: 25px;
    letter-spacing: 0.5px;
    white-space: nowrap;
  }
  .spine-divider { margin: 14px 0; font-weight: 500; }
  .front-cover {
    width: 545px;
    height: 100%;
    position: relative;
    background: var(--navy);
    box-shadow: 3px 4px 8px rgba(0,0,0,0.25);
    overflow: hidden;
  }
  .cover-photo {
    position: absolute;
    left: 0; top: 0;
    width: 100%;
    height: 724px;
    background:
      radial-gradient(ellipse 38% 22% at 55% 78%, rgba(127,141,60,0.95), rgba(127,141,60,0) 100%),
      linear-gradient(180deg,
        var(--sky-top) 0%,
        var(--sky-mid) 22%,
        var(--sky-low) 46%,
        #b9cbd6 52%,
        var(--rock-red) 60%,
        #744030 74%,
        var(--rock-red) 88%,
        var(--rock-dark) 100%);
  }
  .cover-title {
    position: absolute;
    left: 0; right: 0;
    text-align: center;
    color: var(--white);
  }
  .title-top {
    top: 46px;
    font-family: "Cinzel", serif;
    font-weight: 600;
    font-size: 62px;
    line-height: 1;
  }
  .title-main {
    top: 112px;
    font-family: "Oswald", sans-serif;
    font-weight: 600;
    font-size: 100px;
    line-height: 1.05;
    letter-spacing: 1px;
  }
  .title-rule {
    position: absolute;
    left: 141px;
    width: 264px;
    top: 240px;
    height: 2px;
    background: var(--rule);
  }
  .subtitle {
    position: absolute;
    left: 0; right: 0;
    top: 262px;
    text-align: center;
    color: var(--white);
    font-family: "Cinzel", serif;
    font-weight: 600;
    font-size: 20px;
    letter-spacing: 0.5px;
  }
  .author-band {
    position: absolute;
    left: 0; right: 0;
    top: 724px;
    bottom: 0;
    border-top: 6px solid var(--white);
    background: var(--navy-deep);
    display: flex;
    align-items: center;
    justify-content: center;
  }
  .author-name {
    color: var(--white);
    font-family: "Cinzel", serif;
    font-weight: 600;
    font-size: 29px;
    letter-spacing: 0.5px;
    white-space: nowrap;
  }
</style>
</head>
<body>
  <main class="book-spread">
    <section class="spine">
      <p class="spine-text">BEYOND THE TIDEWATER<span class="spine-divider">|</span>DR. MARCUS J. HOLLOWAY</p>
    </section>
    <section class="front-cover">
      <div class="cover-photo" role="img" aria-label="Photograph of a green valley floor between tall red-rock mountains under a blue sky with light clouds"></div>
      <h1>
        <span class="cover-title title-top">BEYOND THE</span>
        <span class="cover-title title-main">TIDEWATER</span>
      </h1>
      <div class="title-rule"></div>
      <p class="subtitle">WALKING FAITH THROUGH RIVERS</p>
      <div class="author-band">
        <p class="author-name">DR. MARCUS J. HOLLOWAY</p>
      </div>
    </section>
  </main>
</body>
</html>
```